Window posters

We want a design (Smiley tooth shaped/logo attached) that will be posted on a dental office windows (23"x23") with 11 different wording/colors for each tooth.
All 11 will have the office name on top (Maple lane grins) then:
1- Friendly dental place, Family dentistry.
2- Comprehensive, periodic, exams, cleanings, X-rays
3- Urgent care dentistry, dental emergencies, dental pain.
4- Extractions, immediate Guided implants, 3D scans.
5- Painless one day root canal treatment, conservative dentistry.
6- Cosmetic dentistry, bonding, digital smile makeover.
7- Clear aligners, True beam, Clarofit.
8- Same day crowns and bridges.
9- Partial and complete dentures, implants Overdenture.
10- All teeth fixed on Implants.
11- Sleep apnea appliances, sleep dentistry.

```html
<!DOCTYPE html>
<html lang="en">
<head>
<meta charset="utf-8">
<title>Maple lane grins — Window posters</title>
<link rel="stylesheet" href="https://fonts.googleapis.com/css2?family=Open+Sans:wght@700&display=swap">
<style>
  :root {
    --page: #ffffff;
    --card: #ffffff;
    --brand: #315a9e;
    --purple: #5a10d4;
    --teal: #10d3c4;
    --pink: #ea6bf0;
    --indigo: #4a52a6;
    --rust: #bf5a48;
    --olive: #a8a84b;
    --green: #4aa878;
    --yellow: #f0cd69;
    --blue: #315a9e;
    --orange: #d4540f;
  }
  * { box-sizing: border-box; margin: 0; padding: 0; }
  html, body {
    width: 1200px;
    height: 1200px;
    overflow: hidden;
    background: var(--page);
    font-family: "Open Sans", Arial, sans-serif;
  }
  .poster-sheet {
    position: relative;
    width: 1200px;
    height: 1200px;
  }
  .poster {
    position: absolute;
    width: 364px;
    height: 364px;
    background: var(--card);
    box-shadow: 0 14px 22px rgba(0, 0, 0, 0.13);
    text-align: center;
  }
  .poster--r1 { top: 32px; }
  .poster--r2 { top: 416px; }
  .poster--r3 { top: 801px; }
  .poster--left { left: 204px; }
  .poster--right { left: 632px; }

  .office-name {
    position: absolute;
    top: 40px;
    left: 0;
    right: 0;
    font-size: 22px;
    font-weight: 700;
    color: var(--brand);
    letter-spacing: 0.2px;
  }
  .tooth-mark {
    position: absolute;
    top: 100px;
    left: 127px;
    width: 110px;
    height: 110px;
    border-radius: 50%;
  }
  .service {
    position: absolute;
    left: 0;
    right: 0;
    font-weight: 700;
  }

  .poster--checkups .tooth-mark { background: var(--teal); }
  .poster--checkups .service { color: var(--purple); top: 236px; font-size: 22px; line-height: 35px; }

  .poster--rootcanal .tooth-mark { background: var(--pink); }
  .poster--rootcanal .service { color: var(--indigo); top: 246px; font-size: 20px; line-height: 31px; }

  .poster--cosmetic .tooth-mark { background: var(--olive); }
  .poster--cosmetic .service { color: var(--rust); top: 245px; font-size: 20px; line-height: 32px; }

  .poster--implants .tooth-mark { background: var(--yellow); }
  .poster--implants .service { color: var(--green); top: 245px; font-size: 20px; line-height: 32px; }

  .poster--family .tooth-mark { background: var(--blue); }
  .poster--family .service { color: var(--blue); top: 262px; font-size: 28px; line-height: 42px; }

  .poster--urgent .tooth-mark { background: var(--purple); }
  .poster--urgent .service { color: var(--orange); top: 242px; font-size: 23px; line-height: 35px; }
</style>
</head>
<body>
<main class="poster-sheet">

  <section class="poster poster--r1 poster--left poster--checkups">
    <h2 class="office-name">Maple lane grins</h2>
    <div class="tooth-mark" role="img" aria-label="Office tooth emblem"></div>
    <p class="service">Comprehensive,<br>periodic, exams,<br>cleanings, X-rays</p>
  </section>

  <section class="poster poster--r1 poster--right poster--rootcanal">
    <h2 class="office-name">Maple lane grins</h2>
    <div class="tooth-mark" role="img" aria-label="Office tooth emblem"></div>
    <p class="service">Painless one-day<br>root canal treatment,<br>conservative dentistry</p>
  </section>

  <section class="poster poster--r2 poster--left poster--cosmetic">
    <h2 class="office-name">Maple lane grins</h2>
    <div class="tooth-mark" role="img" aria-label="Office tooth emblem"></div>
    <p class="service">Cosmetic dentistry,<br>bonding,<br>digital smile makeover</p>
  </section>

  <section class="poster poster--r2 poster--right poster--implants">
    <h2 class="office-name">Maple lane grins</h2>
    <div class="tooth-mark" role="img" aria-label="Office tooth emblem"></div>
    <p class="service">Extractions,<br>immediate Guided implants,<br>3D scans</p>
  </section>

  <section class="poster poster--r3 poster--left poster--family">
    <h2 class="office-name">Maple lane grins</h2>
    <div class="tooth-mark" role="img" aria-label="Office tooth emblem"></div>
    <p class="service">Friendly dental place,<br>Family dentistry</p>
  </section>

  <section class="poster poster--r3 poster--right poster--urgent">
    <h2 class="office-name">Maple lane grins</h2>
    <div class="tooth-mark" role="img" aria-label="Office tooth emblem"></div>
    <p class="service">Urgent care dentistry,<br>dental emergencies,<br>dental pain</p>
  </section>

</main>
</body>
</html>
```